Business Card and Letterhead for Nurlo - modern real estate business

I need a double sided business card design for Nurlo. Please see business card brief here https://papers.trelvimo.net/sheet/q/7XrTbaLeZpMmQ2uWvd9HkCj4yNoEfsGi3lRtAz_pk/view?mode=shared

Please feel free to design the business cards however you feel best. I am happy to give some creative freedoms and then provide feedback from there.

Please then also create a letterhead to match the business card design

Colors

Designer to choose colors to be used in the design.

Requirements
Must have
• Must be a modern, elegant business card which looks very professional

```html
<!DOCTYPE html>
<html lang="en">
<head>
<meta charset="utf-8">
<title>Nurlo Business Card</title>
<link rel="stylesheet" href="https://fonts.googleapis.com/css2?family=Exo+2:wght@400;600;700&display=swap">
<style>
  :root {
    --backdrop: #1c1c1c;
    --card-white: #ffffff;
    --card-dark: #282828;
    --brand-red: #e30613;
    --ink: #2b2b2b;
    --ink-soft: #4a4a4a;
    --stripe-edge: #1a1a1a;
    --photo-top: #e9e6e4;
    --photo-bottom: #3a3a3c;
  }
  * { margin: 0; padding: 0; box-sizing: border-box; }
  html, body {
    width: 1125px; height: 1200px; overflow: hidden;
    background: var(--backdrop);
    font-family: "Exo 2", sans-serif;
  }
  .card {
    position: absolute; left: 171px; width: 826px; height: 472px;
    box-shadow: 0 6px 18px rgba(0,0,0,0.5);
  }
  .card--front { top: 106px; background: var(--card-white); overflow: hidden; }
  .card--back { top: 640px; background: var(--card-dark); }

  .side-stripe {
    position: absolute; left: 33px; top: 0; width: 47px; height: 100%;
    background: var(--brand-red);
    border-left: 3px solid var(--stripe-edge);
    border-right: 3px solid var(--stripe-edge);
  }
  .icon { position: absolute; left: 48px; width: 18px; height: 18px; }
  .icon svg { width: 100%; height: 100%; fill: #fff; }

  .wordmark {
    position: absolute; color: var(--brand-red);
    font-weight: 700; letter-spacing: 0.04em; line-height: 1;
  }
  .card--front .wordmark { left: 112px; top: 64px; font-size: 66px; }
  .card--back .wordmark {
    left: 0; right: 0; top: 200px; text-align: center; font-size: 104px;
  }

  .agent-name {
    position: absolute; left: 113px; top: 220px;
    font-size: 25px; font-weight: 600; color: var(--brand-red);
  }
  .agent-role {
    position: absolute; left: 114px; top: 251px;
    font-size: 16px; font-weight: 600; color: var(--ink);
  }
  .contact {
    position: absolute; left: 115px;
    font-size: 17px; font-weight: 400; color: var(--ink-soft); line-height: 1.3;
  }
  .contact--small { font-size: 16px; }

  .agent-photo {
    position: absolute; right: 0; bottom: 0; width: 398px; height: 424px;
    background: linear-gradient(180deg, var(--photo-top) 0%, #bfb2aa 30%, var(--photo-bottom) 60%, #2a2a2c 100%);
    border-radius: 160px 160px 0 0;
  }
</style>
</head>
<body>
  <section class="card card--front">
    <div class="side-stripe"></div>

    <div class="icon" style="top:224px">
      <svg viewBox="0 0 20 20"><circle cx="10" cy="6" r="4.5"/><path d="M1 19c0-5 4-8 9-8s9 3 9 8z"/></svg>
    </div>
    <div class="icon" style="top:297px">
      <svg viewBox="0 0 20 20"><path d="M10 1a6.5 6.5 0 0 0-6.5 6.5C3.5 12 10 19 10 19s6.5-7 6.5-11.5A6.5 6.5 0 0 0 10 1zm0 9a2.5 2.5 0 1 1 0-5 2.5 2.5 0 0 1 0 5z"/></svg>
    </div>
    <div class="icon" style="top:361px">
      <svg viewBox="0 0 20 20"><path d="M4 1l4 4-2 3c1 2.5 3.5 5 6 6l3-2 4 4-3 3C8 18 2 12 1 4z"/></svg>
    </div>
    <div class="icon" style="top:388px">
      <svg viewBox="0 0 20 20"><path d="M1 4h18v12H1z M2 5l8 6 8-6" stroke="#e30613" stroke-width="1.6"/></svg>
    </div>
    <div class="icon" style="top:410px">
      <svg viewBox="0 0 20 20"><circle cx="10" cy="10" r="8.5"/><path d="M5 6l3 1 1 3-2 2 1 4M12 3l1 3 3 1M13 12l2 3" stroke="#e30613" stroke-width="1.5" fill="none"/></svg>
    </div>

    <div class="wordmark">NURLO</div>

    <h1 class="agent-name">Ryan Dalby</h1>
    <p class="agent-role">Licenced Real Estate Agent</p>

    <p class="contact" style="top:283px">PO Box 7316<br>Larkfield NSW 2790</p>
    <p class="contact" style="top:358px">0451 390 284</p>
    <p class="contact contact--small" style="top:384px">ryan@nurlo.com</p>
    <p class="contact contact--small" style="top:406px">www.nurlo.com</p>

    <div class="agent-photo" role="img" aria-label="Portrait photo of the agent in a dark suit"></div>
  </section>

  <section class="card card--back">
    <div class="wordmark">NURLO</div>
  </section>
</body>
</html>
```